New one page Homepage with registration and log in form

Hi designers!

We need a new homepage and made a skitch of how it should be.

Can you give some of your design ideas and work it out so that it actually looks great?

Its just one page, for convertion reasons.

The logo doesnt have to be changed.

It would be cool to center the logo but not sure how design technically correct that is.

The social icons can be left out.

If you could give a few mockups than we can choose the best one.

I added one screenshot sketch of the homepage.

And 2 screenshots of what the system looks like on the inside, just so you get an idea.

Thanks

Target Market(s)

Vacation rental owners who want to increase their bookings by connecting with other VR owners and managers, or by having their own booking team for a small fee.

Industry/Entity Type

Social

Number of Pages Required

1 page

Requirements
Must have
• Use your imagination please
Nice to have
• Use your imagination
• It will be a one page design so we need to impress :)
• Keep it compact, maybe a web 3.0 flat design, etc
Should not have
• Other pages.

```html
<!DOCTYPE html>
<html lang="en">
<head>
<meta charset="utf-8">
<title>StayHaven – The First Social Booking Network</title>
<link href="https://fonts.googleapis.com/css2?family=Arimo:wght@400;700&display=swap" rel="stylesheet">
<style>
:root{
  --ink:#1a1a1a;
  --topbar:#262626;
  --brand-blue:#0a3d85;
  --hero-blue:#003a80;
  --hero-blue-light:#2b5d9e;
  --accent-line:#1c72b0;
  --orange:#ff5f00;
  --panel:#ebebeb;
  --field:#e4e4e4;
  --field-border:#d4d4d4;
  --placeholder:#8a8a8a;
  --submit:#0048a6;
  --social-btn:#2f5395;
  --link:#1046a0;
  --footer:#000;
  --footer-text:#8c8c8c;
  --circle-a:#2f5395;
  --circle-b:#1a84c4;
  --circle-c:#d6352b;
}
*{box-sizing:border-box;margin:0;padding:0}
html,body{width:1200px;height:1130px;overflow:hidden}
body{font-family:"Arimo",Arial,sans-serif;color:var(--ink);background:#fff;position:relative}
.topbar{position:absolute;left:0;top:0;width:1200px;height:6px;background:var(--topbar)}
.site-header{position:absolute;left:0;top:6px;width:1200px;height:109px;background:#fff;border-bottom:4px solid var(--accent-line)}
.brand{position:absolute;left:104px;top:32px;display:flex;align-items:center;gap:12px}
.brand-dot{width:30px;height:30px;border-radius:50%;background:var(--orange)}
.brand-name{font-size:36px;font-weight:700;color:var(--brand-blue);letter-spacing:.5px}
.social{position:absolute;right:100px;top:34px;display:flex;gap:19px}
.social span{display:block;width:45px;height:45px;border-radius:50%}
.social .s1{background:var(--circle-a)}
.social .s2{background:var(--circle-b)}
.social .s3{background:var(--circle-c)}
.hero{position:absolute;left:0;top:119px;width:1200px;height:389px;background:var(--hero-blue)}
.hero-crowd{position:absolute;inset:0;background:linear-gradient(180deg,var(--hero-blue) 0%,var(--hero-blue-light) 45%,var(--hero-blue) 100%);opacity:.9}
.player{position:absolute;left:100px;top:69px;width:433px;height:262px;background:#000;box-shadow:0 2px 6px rgba(0,0,0,.6);overflow:hidden}
.player-gloss{position:absolute;right:0;top:0}
.player-bar{position:absolute;left:14px;bottom:10px;width:400px;height:24px;background:#111;border:1px solid #333;display:flex;align-items:center;color:#fff;font-size:9px;font-weight:700}
.pause{width:7px;height:9px;margin:0 12px;border-left:2px solid #fff;border-right:2px solid #fff}
.track{width:206px;height:2px;background:#555;margin-left:2px;position:relative}
.track::before{content:"";position:absolute;left:0;top:0;width:132px;height:2px;background:#fff}
.time{margin-left:24px}
.vol{margin-left:12px;width:8px;height:8px;background:#ddd}
.hq{margin-left:8px;padding:1px 3px;border:1px solid #aaa;font-size:7px}
.full{margin-left:6px;width:20px;height:12px;background:#777}
.hero-copy{position:absolute;left:590px;top:22px;width:500px;color:#fff}
.hero-copy h1{font-size:38px;font-weight:700;line-height:47px;letter-spacing:.2px}
.hero-copy p{font-size:14px;line-height:19px;margin-top:19px}
.hero-copy h1+p{margin-top:18px}
.section-title{position:absolute;font-size:24px;font-weight:400}
.login-title{left:101px;top:550px;color:var(--orange)}
.register-title{left:661px;top:550px;color:var(--brand-blue)}
.register-sub{position:absolute;left:662px;top:582px;font-size:12px;letter-spacing:.5px}
.panel{position:absolute;top:608px;width:440px;height:400px;background:var(--panel)}
.panel::after{content:"";position:absolute;left:20px;right:28px;bottom:-14px;height:14px;background:radial-gradient(ellipse at top,rgba(0,0,0,.15),transparent 70%)}
.login-panel{left:100px}
.register-panel{left:660px}
.field{position:absolute;height:32px;background:var(--field);border:1px solid var(--field-border);box-shadow:inset 0 1px 2px rgba(0,0,0,.06);font-size:13px;color:var(--placeholder);padding:8px 18px;line-height:15px}
.remember{position:absolute;left:26px;top:134px;display:flex;align-items:center;gap:12px;font-size:13px}
.remember span{width:16px;height:16px;background:#d0d0d0;border:1px solid #c4c4c4}
.btn{position:absolute;height:34px;color:#fff;font-size:14px;font-weight:700;display:flex;align-items:center;justify-content:center}
.btn-login{left:26px;top:188px;width:379px;background:var(--orange)}
.btn-submit{left:27px;top:330px;width:378px;background:var(--submit)}
.social-label{position:absolute;left:0;width:418px;top:246px;text-align:center;font-size:13px}
.btn-social{left:91px;top:297px;width:236px;height:40px;background:var(--social-btn);border:1px solid #1d3566;border-radius:4px;font-size:17px;gap:12px}
.btn-social i{width:18px;height:18px;background:#fff;display:block}
.forgot{position:absolute;left:0;width:402px;top:361px;text-align:center;font-size:12px;color:var(--link);letter-spacing:.3px}
.site-footer{position:absolute;left:0;top:1050px;width:1200px;height:80px;background:var(--footer)}
.site-footer p{position:absolute;left:549px;top:33px;font-size:12px;color:var(--footer-text);letter-spacing:.6px}
</style>
</head>
<body>
<div class="topbar"></div>
<header class="site-header">
  <div class="brand"><span class="brand-dot"></span><span class="brand-name">StayHaven</span></div>
  <nav class="social" aria-label="Social links"><span class="s1"></span><span class="s2"></span><span class="s3"></span></nav>
</header>

<section class="hero">
  <div class="hero-crowd" role="img" aria-label="Group of smiling people standing together, tinted blue"></div>
  <div class="player">
    <svg class="player-gloss" width="100" height="80" viewBox="0 0 100 80"><polygon points="0,0 100,0 100,80" fill="#3a3a3a" opacity=".7"/></svg>
    <div class="player-bar">
      <span class="pause"></span><span class="track"></span><span class="time">0:45 / 1:36</span>
      <span class="vol"></span><span class="hq">HQ</span><span class="full"></span>
    </div>
  </div>
  <div class="hero-copy">
    <h1>The First<br>Social Booking Network</h1>
    <p>StayHaven is a new Social Booking Network.<br>Vacation rental hosts and property managers can find each other,connect and chat amongst themselves for sharing reservation inquiries,services or anything you can imagine,in a convenient social environment.</p>
    <p>The Social Booking Network is absolutely FREE. However if you want to save time and get really professional about incresing your bookings.Than you should consider having your own Booking Team.</p>
    <p>For just 2.5% your very own StayHaven team take care of all tedious online reservation management tasks for you in the most advanced,personalized and professional way possible.</p>
  </div>
</section>

<h2 class="section-title login-title">Login to your account</h2>
<h2 class="section-title register-title">Don't have an account?</h2>
<p class="register-sub">Register now to join the Free Booking Network !</p>

<form class="panel login-panel">
  <div class="field" style="left:26px;top:41px;width:379px">Your username or email address</div>
  <div class="field" style="left:26px;top:87px;width:379px">Your password</div>
  <label class="remember"><span></span>Would you like us to remember you?</label>
  <div class="btn btn-login">Log me in</div>
  <p class="social-label">Sign in with your social identity</p>
  <div class="btn btn-social"><i></i>Login with Socialbook</div>
  <p class="forgot">I forgot my username / Password</p>
</form>

<form class="panel register-panel">
  <div class="field" style="left:26px;top:41px;width:179px">First Name</div>
  <div class="field" style="left:226px;top:41px;width:179px">Last Name</div>
  <div class="field" style="left:26px;top:87px;width:379px">Username</div>
  <div class="field" style="left:26px;top:134px;width:379px">Password</div>
  <div class="field" style="left:26px;top:183px;width:379px">user@email.com</div>
  <div class="field" style="left:26px;top:231px;width:379px">Set your contact number . Example:+12345678910</div>
  <div class="field" style="left:26px;top:278px;width:379px">What's your reason for joing?</div>
  <div class="btn btn-submit">Submit</div>
</form>

<footer class="site-footer"><p>copyright 2014</p></footer>
</body>
</html>
```